creation of business cards for Velanto Sàrl

Velanto S% 26 # 224; rl is a soci% 26 # 233; t% 26 # 233; consultancy that accompanies companies in the development of their business on the market% 26 # 233; Switzerland by providing strategic contacts or market information; and by providing administrative or logistical support. Our consulting skills focus on sectors% 26 # 224; high value added% 26 # 233; e, such as trade in food goods% 26 # 39amp; drinks, fashion% 26amp; lifestyle, products and services for% 26 # 233; s in high-tech industries (pharmaceutical, chemical, m% 26 # 233; pricy 26% 23 #; cision) or sustainable solutions (% 26 # 233; energies renewable, mat% 26 # 233; recyclable materials). As part of the launch of our activity% 26 # 233;, we need% 26 # 39;% 26 # 233; to establish business cards to d% 26 # 233; work our new customers (Swiss or international).

Target Market(s)

Companies wishing to develop their activity% 26 # 233; s in Switzerland or% 26 # 224; l% 26 # 39;% 26 # 233; abroad (mainly in Europe).

Contact Information for Business Card

Prénom NOM
Velanto Sàrl
Bureau de Marvoisin
Rue des Tilleuls 47, 2000 Neuchâtel
Tél. : 032 718 46 39
info@velanto-example.ch
www.velanto-example.ch

Font styles to use
Serif
Sans Serif

Colors

Designer to choose colors to be used in the design.

Requirements
Must have
• The logo The name of the company% 26 # 233; t% 26 # 233; (Velanto S% 26 # 224; rl) One field for the mailing address One field for the number% 26 # 233; ro de t% 26 # 233; l% 26 # 233; phone One field for the % 26 # 39; email address and website

```html
<!DOCTYPE html>
<html lang="fr">
<head>
<meta charset="utf-8">
<title>Velanto Sàrl – cartes de visite</title>
<link rel="stylesheet" href="https://fonts.googleapis.com/css2?family=Montserrat:wght@300&family=Roboto:wght@400;700&display=swap">
<style>
  :root {
    --teal: #00435a;
    --white: #ffffff;
    --paper: #f4f5f6;
    --name-grey: #a9b6bf;
    --backdrop: #cfd2d5;
    --shadow: rgba(0, 0, 0, 0.22);
  }
  * { box-sizing: border-box; margin: 0; padding: 0; }
  html, body { width: 1200px; height: 800px; overflow: hidden; }
  body {
    background: var(--backdrop);
    position: relative;
    font-family: "Roboto", Arial, sans-serif;
  }
  .card {
    position: absolute;
    width: 520px;
    height: 300px;
    border-radius: 22px;
    overflow: hidden;
    box-shadow: 0 6px 18px var(--shadow);
  }

  /* Back side */
  .card-back {
    left: 580px;
    top: 90px;
    background: var(--teal);
    display: flex;
    align-items: center;
    justify-content: center;
    gap: 18px;
  }
  .brand-square {
    width: 40px;
    height: 40px;
    border-radius: 9px;
    background: var(--white);
  }
  .brand-name {
    font-family: "Montserrat", Arial, sans-serif;
    font-weight: 300;
    font-size: 36px;
    letter-spacing: 5px;
    color: var(--white);
  }

  /* Front side */
  .card-front {
    left: 100px;
    top: 410px;
    background: var(--teal);
  }
  .front-panel {
    position: absolute;
    left: 0; top: 0;
    width: 195px;
    height: 100%;
    background: var(--paper);
  }
  .front-brand {
    position: absolute;
    left: 68px;
    top: 150px;
    transform: translate(-50%, -50%) rotate(-90deg);
    font-family: "Montserrat", Arial, sans-serif;
    font-weight: 300;
    font-size: 40px;
    letter-spacing: 5px;
    color: var(--teal);
    white-space: nowrap;
  }
  .front-square {
    position: absolute;
    left: 130px;
    top: 78px;
    width: 130px;
    height: 126px;
    border-radius: 30px;
    background: var(--teal);
    border: 5px solid var(--white);
  }
  .contact {
    position: absolute;
    left: 290px;
    top: 52px;
    color: var(--white);
    font-size: 14.5px;
    line-height: 1.25;
  }
  .contact-name {
    font-weight: 700;
    font-size: 19px;
    color: var(--name-grey);
  }
  .contact-role {
    margin-bottom: 14px;
  }
  .contact-address { margin-bottom: 8px; }
  .contact-line {
    display: flex;
    align-items: center;
    gap: 6px;
  }
  .contact-line svg { width: 12px; height: 12px; flex: none; }
</style>
</head>
<body>

  <section class="card card-back" aria-label="Verso de la carte">
    <span class="brand-square"></span>
    <span class="brand-name">VELANTO</span>
  </section>

  <section class="card card-front" aria-label="Recto de la carte">
    <div class="front-panel"></div>
    <span class="front-brand">VELANTO</span>
    <span class="front-square"></span>

    <div class="contact">
      <p class="contact-name">Laurent Dubois</p>
      <p class="contact-role">President</p>
      <p class="contact-address">
        Velanto Sàrl<br>
        Bureau de Marvoisin<br>
        Rue des Tilleuls 47<br>
        2000 Neuchâtel
      </p>
      <p class="contact-line">
        <svg viewBox="0 0 12 12"><path d="M2.5 1 L4.5 1 L5.3 3.6 L4 4.6 Q5 7 7.4 8 L8.4 6.7 L11 7.5 L11 9.5 Q10.5 11 9 11 Q1 10 1 2.8 Q1 1.4 2.5 1 Z" fill="#cfd8de"/></svg>
        032 718 46 39
      </p>
      <p class="contact-line">
        <svg viewBox="0 0 12 12"><rect x="0.8" y="2.5" width="10.4" height="7" fill="none" stroke="#cfd8de" stroke-width="1"/><path d="M0.8 2.5 L6 6.5 L11.2 2.5" fill="none" stroke="#cfd8de" stroke-width="1"/></svg>
        info@velanto-example.ch
      </p>
      <p class="contact-line">
        <svg viewBox="0 0 12 12" fill="none" stroke="#cfd8de" stroke-width="0.9"><circle cx="6" cy="6" r="5"/><ellipse cx="6" cy="6" rx="2.2" ry="5"/><path d="M1 6 H11 M2 3.3 H10 M2 8.7 H10"/></svg>
        www.velanto-example.ch
      </p>
    </div>
  </section>

</body>
</html>
```